Staffing and Consulting Service Company needs Business Cards

We need to have business cards for our business. You can check our website www.talvrenix.com to see the branding we are using. The logo is in the website.
We use a tag line Staffing & Consulting Solutions Made Easy.
We use different blues in the logo and we use the red for the Company name.
As you can see in the website there is a gradient in the bottom part of each page that includes some of the dots we use for the logo.
We will need the following fields on the design:
Company Name
Employee Name
Title
Address
Tel
Email
Website
Can be Single or Double Sided
There is no preference for single or double sided.
Target Market(s)
Companies in need of IT staffing and IT consulting services
Industry/Entity Type
Business
Look and feel

```html
<!DOCTYPE html>
<html lang="en">
<head>
<meta charset="utf-8">
<title>Talvrenix Business Card</title>
<link rel="stylesheet" href="https://fonts.googleapis.com/css2?family=Cinzel:wght@400&family=Questrial&display=swap">
<style>
  :root {
    --stage: #ecebe8;
    --navy-deep: #1f2157;
    --navy: #34387e;
    --periwinkle: #7c80bf;
    --lavender: #b7b9e0;
    --brand-red: #7c2b30;
    --text-blue: #262a66;
    --paper: #ffffff;
    --mist: #e6e6ea;
  }
  * { box-sizing: border-box; margin: 0; padding: 0; }
  html, body { width: 1200px; height: 784px; overflow: hidden; background: var(--stage); }
  .canvas {
    width: 1200px; height: 784px;
    display: flex; align-items: center; justify-content: center; gap: 40px;
  }
  .card {
    position: relative; width: 540px; height: 310px; overflow: hidden;
    box-shadow: 0 6px 18px rgba(0,0,0,.18);
  }
  /* back side */
  .card-back {
    background: linear-gradient(100deg, var(--navy-deep) 0%, var(--navy) 45%, #5a5ea6 100%);
  }
  .back-dot-field {
    position: absolute; inset: 0;
    background:
      radial-gradient(ellipse 70% 90% at 85% 40%, rgba(183,185,224,.55), rgba(124,128,191,.15) 60%, transparent 80%);
  }
  .back-website {
    position: absolute; left: 60px; top: 140px;
    font-family: "Questrial", sans-serif; font-size: 19px;
    letter-spacing: 7px; color: var(--paper);
  }
  /* front side */
  .card-front { background: var(--paper); }
  .front-dot-field {
    position: absolute; right: 20px; top: 30px; width: 210px; height: 150px;
    background: radial-gradient(ellipse at center, var(--mist) 0%, rgba(230,230,234,.5) 55%, transparent 75%);
  }
  .swoosh { position: absolute; left: 0; bottom: 0; width: 540px; height: 200px; z-index: 0; }
  .brand {
    position: absolute; left: 30px; top: 32px; z-index: 1;
    display: flex; align-items: center; gap: 10px;
  }
  .brand-square { width: 58px; height: 58px; background: var(--navy); border-radius: 6px; }
  .brand-name {
    font-family: "Cinzel", serif; font-size: 44px; color: var(--brand-red);
    letter-spacing: 1px; line-height: 1;
  }
  .person { position: absolute; left: 46px; top: 110px; z-index: 1; font-family: "Questrial", sans-serif; }
  .person-name { font-size: 17px; color: var(--brand-red); font-weight: 700; }
  .person-title { font-size: 10px; color: var(--text-blue); line-height: 1.25; margin-top: 2px; margin-left: 6px; }
  .contact {
    position: absolute; left: 52px; top: 164px; z-index: 1; list-style: none;
    font-family: "Questrial", sans-serif; font-size: 14px; color: var(--text-blue);
  }
  .contact li { display: flex; align-items: center; gap: 7px; height: 18px; }
  .contact svg { width: 12px; height: 12px; fill: var(--brand-red); flex: none; }
  .contact .indent { padding-left: 19px; }
</style>
</head>
<body>
<main class="canvas">
  <section class="card card-back" aria-label="Card back">
    <div class="back-dot-field" role="img" aria-label="Brand dot pattern fading across the navy background"></div>
    <p class="back-website">www.talvrenix.com</p>
  </section>

  <section class="card card-front" aria-label="Card front">
    <div class="front-dot-field" role="img" aria-label="Faint grey brand dot pattern"></div>
    <svg class="swoosh" viewBox="0 0 540 200" aria-hidden="true">
      <path d="M150 200 C320 178 450 120 540 20 L540 200 Z" fill="#ffffff"/>
      <path d="M130 196 C320 172 450 112 540 10 L540 28 C450 130 330 182 130 199 Z" fill="var(--lavender)"/>
      <path d="M110 200 C320 180 450 124 540 38 L540 66 C450 148 330 192 160 200 Z" fill="var(--periwinkle)"/>
      <path d="M250 200 C380 186 470 150 540 84 L540 96 C470 160 390 194 300 200 Z" fill="var(--navy)"/>
    </svg>
    <div class="brand">
      <span class="brand-square"></span>
      <span class="brand-name">TALVRENIX</span>
    </div>
    <div class="person">
      <p class="person-name">Marcus D. Okonkwo</p>
      <p class="person-title">Senior Technical Recruiting &amp;<br>Business Development Manager</p>
    </div>
    <ul class="contact">
      <li><svg viewBox="0 0 12 12"><path d="M2 1h3l1 3-2 1a7 7 0 0 0 3 3l1-2 3 1v3c0 1-1 1-1 1C5 11 1 7 1 2c0 0 0-1 1-1z"/></svg>954.555.0142</li>
      <li><svg viewBox="0 0 12 12"><rect x="3" y="0" width="6" height="12" rx="1"/><rect x="4" y="1.5" width="4" height="6" fill="#fff"/></svg>305.555.0187</li>
      <li><svg viewBox="0 0 12 12"><rect x="1" y="4" width="10" height="7" rx="1"/><rect x="3" y="0" width="6" height="4" fill="none" stroke="var(--brand-red)"/></svg>954.555.0142</li>
      <li><svg viewBox="0 0 12 12"><rect x="0" y="2" width="12" height="8" rx="1"/><path d="M0 2l6 5 6-5" fill="none" stroke="#fff"/></svg>marcusd@talvrenix.com</li>
      <li><svg viewBox="0 0 12 12"><path d="M6 0l6 6h-2v6H7V8H5v4H2V6H0z"/></svg>4410 NW 88th TER</li>
      <li class="indent">Sunrise, FL 33351</li>
    </ul>
  </section>
</main>
</body>
</html>
```